Brandvale Site Oversight Group Inc. needs a logo design (BSOGI) and a business card design

We need a logo design and business card design for a new company. Simple yet elegant/stylish and professional. to the point. Focal point BRANDVALE...underneith Site Oversight Group Inc smaller font. Plus a logo that can be on the opposite side of the business card and used for T-Shirts.
Back back ground, silver/grey font. I like the look of Quirtle Studio logo
Target Market(s)
Project controls, Planning, Scheduling, Engineering, Project Management
Industry/Entity Type
Business
Contact Information for Business Card
Company name on one side, logo and details on the other
Font styles to use
Requirements
Must have
- Delphine Brandvale
- Project Planner
- BrandvaleSOGI@postmarrow.example
- P.O. Box 9
- Dunmere QX NORLAND
- X9Q2R7
- +1 (555) 284 3917
Nice to have
- Your input :) quote "Fail to plan, plan to fail"
Should not have
- Too much!

```html
<!DOCTYPE html>
<html lang="en">
<head>
<meta charset="utf-8">
<title>Brandvale Site Oversight Group – Identity</title>
<link rel="stylesheet" href="https://fonts.googleapis.com/css2?family=League+Spartan:wght@400;600;700&family=Yellowtail&family=Crimson+Text:ital@1&display=swap">
<style>
  :root {
    --page: #ffffff;
    --ink: #333132;
    --ink-soft: #5f5e60;
    --label: #2b2b2b;
    --dark-card-a: #2b2828;
    --dark-card-b: #1b1919;
    --silver: #d9d9d9;
    --silver-soft: #b9b9b9;
    --light-card-a: #fbfbfb;
    --light-card-b: #e9e9e9;
  }
  * { margin: 0; padding: 0; box-sizing: border-box; }
  html, body { width: 720px; height: 1200px; overflow: hidden; background: var(--page); }
  body { font-family: "League Spartan", sans-serif; color: var(--ink); }

  .sheet { width: 720px; height: 1200px; display: flex; flex-direction: column; justify-content: center; gap: 64px; padding: 0 30px; }

  .card-row { display: flex; justify-content: space-between; }
  .card-slot { width: 320px; display: flex; flex-direction: column; align-items: center; gap: 10px; }
  .slot-label { font-family: "Yellowtail", cursive; font-size: 24px; line-height: 1.2; color: var(--label); white-space: nowrap; }

  .card { width: 320px; height: 178px; position: relative; box-shadow: 0 4px 10px rgba(0,0,0,.35); overflow: hidden; }
  .card--dark { background: linear-gradient(135deg, var(--dark-card-a), var(--dark-card-b)); color: var(--silver); }
  .card--light { background: linear-gradient(135deg, var(--light-card-a), var(--light-card-b)); color: var(--ink); }

  /* front */
  .card-front { display: flex; align-items: center; padding: 0 12px 0 18px; gap: 18px; }
  .name-block { flex: 0 0 122px; text-align: center; padding: 9px 0; border-top: 1.5px solid currentColor; border-bottom: 1.5px solid currentColor; }
  .name { font-weight: 700; font-size: 15px; line-height: 1.1; letter-spacing: .3px; }
  .role { font-size: 11px; margin-top: 3px; white-space: nowrap; }
  .contact { font-size: 9px; line-height: 1.25; white-space: nowrap; }
  .contact .email { margin-bottom: 9px; }
  .contact .phone { margin-top: 9px; }

  /* back */
  .card-back { display: flex; flex-direction: column; align-items: center; justify-content: center; padding-bottom: 14px; }
  .card-back .wordmark { font-size: 34px; }
  .card-back .tagline { font-size: 12px; gap: 6px; margin-top: 3px; }
  .card-back .tagline::before, .card-back .tagline::after { width: 24px; height: 2px; }
  .quote { position: absolute; bottom: 24px; font-family: "Crimson Text", serif; font-style: italic; font-size: 10.5px; }
  .card--dark .quote, .card--dark .tagline { color: var(--silver-soft); }

  /* logo */
  .logo { display: flex; flex-direction: column; align-items: center; }
  .wordmark { font-weight: 700; letter-spacing: .5px; line-height: 1; white-space: nowrap; }
  .logo .wordmark { font-size: 112px; letter-spacing: 2px; color: var(--ink); }
  .tagline { display: flex; align-items: center; font-weight: 600; font-variant: small-caps; white-space: nowrap; }
  .tagline::before, .tagline::after { content: ""; background: currentColor; border-radius: 2px; }
  .logo .tagline { font-size: 42px; color: var(--ink-soft); gap: 18px; margin-top: 6px; width: 640px; }
  .logo .tagline::before, .logo .tagline::after { flex: 1; height: 5px; background: var(--ink); }
</style>
</head>
<body>
<main class="sheet">

  <section class="card-row">
    <div class="card-slot">
      <p class="slot-label">– black background front –</p>
      <div class="card card--dark card-front">
        <div class="name-block">
          <p class="name">DELPHINE<br>BRANDVALE</p>
          <p class="role">— Project Planner —</p>
        </div>
        <div class="contact">
          <p class="email">BrandvaleSOGI@postmarrow.example</p>
          <p>P.O. Box 9</p>
          <p>Dunmere QX NORLAND</p>
          <p>X9Q2R7</p>
          <p class="phone">+1 (555) 284 3917</p>
        </div>
      </div>
    </div>
    <div class="card-slot">
      <p class="slot-label">– black background back –</p>
      <div class="card card--dark card-back">
        <p class="wordmark">BRANDVALE</p>
        <p class="tagline">Site Oversight Group</p>
        <p class="quote">— Fail to plan, plan to fail —</p>
      </div>
    </div>
  </section>

  <section class="logo">
    <p class="wordmark">BRANDVALE</p>
    <p class="tagline">Site Oversight Group</p>
  </section>

  <section class="card-row">
    <div class="card-slot">
      <p class="slot-label">– light background front –</p>
      <div class="card card--light card-front">
        <div class="name-block">
          <p class="name">DELPHINE<br>BRANDVALE</p>
          <p class="role">— Project Planner —</p>
        </div>
        <div class="contact">
          <p class="email">BrandvaleSOGI@postmarrow.example</p>
          <p>P.O. Box 9</p>
          <p>Dunmere QX NORLAND</p>
          <p>X9Q2R7</p>
          <p class="phone">+1 (555) 284 3917</p>
        </div>
      </div>
    </div>
    <div class="card-slot">
      <p class="slot-label">– light background back –</p>
      <div class="card card--light card-back">
        <p class="wordmark">BRANDVALE</p>
        <p class="tagline">Site Oversight Group</p>
        <p class="quote">— Fail to plan, plan to fail —</p>
      </div>
    </div>
  </section>

</main>
</body>
</html>
```